Greeting card special spring

Context: I missed the end of the year wishes and would like to send my clients a spring card with a smell of lily of the valley that is 11cm by 11 cm and has a vintage look. This A5 card will be sent in a green envelope with the small ordering bag. I will like the target notes the intent and the associated gaiety My business is HR / Leadership and my clients are responsible for business or HR. Esprit: To keep a spirit of sobriete and elegance but with gaiety. Color: our graphic charter is generally black and gray but for this theme we can shift in color more "spring" taking again the green of the sachet of lily of the valley which is joined in particular to illustrate the notions energy, renewal. (Attached the picture). No photo. Just text and logo. Play on composition and fonts; I have put the elements of typos and fonts as well as taglines and examples of compositions already made (business card, correspondence card, letter paper). One of the elements of the graphic chart is an "e" that is done in brush. If you wish you can play with this graphic elements. Also look at the picture of the perfume pouch that I would attach Format: a card a format A5 or format postcard (format printolux). The text is composed of 2 elements: Major Text The Quorvana team wishes you a spring full of renewal, fulfillment and creative energy to disseminate absolutely around you. Text minor: Lily of the Valley: Omen of happiness that brings luck to breathe with serenity! Include Logo See contact details Marthe Lubois-Cagnat - marthe.lubois@quorvana-mail.com

Target Market(s)

Senior managers, human resource managers

Industry/Entity Type

Management Consulting

Other font styles liked:
• merci d'essayer de rester aligner ou en logique avec les polices/charte graphique envoyees

Requirements
Must have
• Format: one card in A5 format or postcard format (printolux format). The text is composed of 2 elements: Major Text The Quorvana team wishes you a spring full of renewal, fulfillment and creative energy to disseminate absolutely around you. Text minor: Lily of the Valley: Omen of happiness that brings luck to breathe with serenity! Include Logo See contact details Marthe Lubois-Cagnat - marthe.lubois@quorvana-mail.com
Nice to have
• Graphical guideline :. Esprit: To keep a spirit of sobriete and elegance but with gaiety. Color: our graphic charter is generally black and gray but for this theme we can shift in color more "spring" taking again the green of the sachet of lily of the valley which is joined in particular to illustrate the notions energy, renewal. (Attached the picture). Grapic elements; I have put the elements of typos and fonts as well as the examples of compositions already made (business card, correspondence card, letter paper). One of the elements of the logo is an "e" that is made in brush on which you can play. Also look at the image of the perfume pouch that I would join
Should not have
• No photo. Just text and logo. Play on composition and fonts

```html
<!DOCTYPE html>
<html lang="fr">
<head>
<meta charset="utf-8">
<title>Quorvana – Carte de printemps</title>
<link rel="stylesheet" href="https://fonts.googleapis.com/css2?family=Parisienne&family=Jost:wght@400&display=swap">
<style>
  :root {
    --frame-green: #9aab47;
    --script-green: #9cab4a;
    --sage-green: #6f8256;
    --paper: #fbfce3;
    --ink: #2a2a2a;
  }
  html, body {
    margin: 0;
    padding: 0;
    width: 847px;
    height: 1200px;
    overflow: hidden;
    background: #ffffff;
  }
  .card {
    position: relative;
    width: 847px;
    height: 1200px;
    box-sizing: border-box;
    border: 13px solid var(--frame-green);
    background: var(--paper);
    text-align: center;
  }
  .wish {
    position: absolute;
    top: 240px;
    left: 0;
    right: 0;
    margin: 0;
    font-family: "Parisienne", cursive;
    font-weight: 400;
    font-size: 64px;
    line-height: 76px;
    color: var(--script-green);
  }
  .omen {
    position: absolute;
    top: 852px;
    left: 0;
    right: 0;
    margin: 0;
    font-family: "Parisienne", cursive;
    font-size: 38px;
    line-height: 45px;
    color: var(--sage-green);
  }
  .brand {
    position: absolute;
    top: 1014px;
    left: 0;
    right: 0;
    display: flex;
    flex-direction: column;
    align-items: center;
  }
  .brand-dot {
    width: 16px;
    height: 16px;
    border-radius: 50%;
    background: var(--ink);
    margin-bottom: 30px;
  }
  .brand-name {
    font-family: "Jost", sans-serif;
    font-size: 11px;
    line-height: 14px;
    letter-spacing: 5px;
    color: var(--ink);
    padding-left: 5px;
  }
  .contact {
    position: absolute;
    top: 1095px;
    left: 0;
    right: 0;
    font-family: "Jost", sans-serif;
    font-size: 11px;
    line-height: 15px;
    color: var(--ink);
    letter-spacing: 0.6px;
  }
</style>
</head>
<body>
  <main class="card">
    <p class="wish">L'équipe de Quorvana<br>vous souhaite un printemps<br>plein de renouveau,<br>d'épanouissement et d'énergie<br>créatrice à diffuser<br>absolument autour<br>de vous.</p>
    <p class="omen">Muguet : présage de bonheur qui porte chance<br>à respirer avec sérénité !</p>
    <div class="brand">
      <span class="brand-dot"></span>
      <span class="brand-name">QUORVANA</span>
    </div>
    <div class="contact">Marthe Lubois-Cagnat<br>marthe.lubois@quorvana-mail.com</div>
  </main>
</body>
</html>
```